Pamphlet for introducing people to our church

I would like a church pamphlet designed, that includes the content in file "vosti-pamphlet.txt".

I am looking for a design that will incorporate the content in a professional and creative manner.

You do not have to use the content in any specific order, but I am relying on your skill and design knowledge to organize everything in an artistic and effective way.

Target Market(s)

Everyone

Industry/Entity Type

Religious

Requirements
Must have
• logo, use of content provided, use of branding (logo colors)
Nice to have
• More images where necessary
Should not have
• cross

```html
<!DOCTYPE html>
<html lang="en">
<head>
<meta charset="utf-8">
<title>Vosti – A Voice to the Nations</title>
<link rel="stylesheet" href="https://fonts.googleapis.com/css2?family=Cinzel:wght@700&family=Dancing+Script:wght@700&family=Kaushan+Script&family=Lato:wght@400;700&display=swap">
<style>
  :root {
    --navy: #0d3560;
    --navy-deep: #0b2f57;
    --blue: #0b4a78;
    --orange: #f7941d;
    --orange-dark: #e5831a;
    --white: #ffffff;
    --paper: #e8e9eb;
    --stage: #d8d9db;
  }
  * { margin: 0; padding: 0; box-sizing: border-box; }
  html, body { width: 921px; height: 1200px; overflow: hidden; background: var(--stage); }
  .canvas { position: relative; width: 921px; height: 1200px; }
  .flyer {
    position: absolute; left: 35.5px; top: 0;
    width: 934px; height: 1318px;
    transform: scale(0.9105); transform-origin: 0 0;
    overflow: hidden; background: var(--navy);
    font-family: "Lato", sans-serif;
  }
  .hero-photo {
    position: absolute; left: 0; top: 0; width: 934px; height: 672px;
    background:
      radial-gradient(ellipse at 30% 25%, rgba(255,240,245,0.95), rgba(230,200,215,0.6) 40%, transparent 70%),
      linear-gradient(180deg, #eadde6 0%, #d9c3cf 35%, #8d7066 60%, #3e3430 85%, #2c2624 100%);
  }
  .backdrop { position: absolute; left: 0; top: 0; width: 934px; height: 1318px; }
  .brand-tab {
    position: absolute; left: 634px; top: 0; width: 279px; height: 240px;
    background: var(--navy-deep); border-radius: 0 0 18px 18px;
    display: flex; align-items: center; justify-content: center; gap: 14px;
  }
  .brand-tab .brand-dot { width: 18px; height: 18px; border-radius: 50%; background: var(--orange); }
  .brand-tab .brand-name { font-family: "Lato", sans-serif; font-weight: 400; font-size: 54px; letter-spacing: 3px; color: var(--white); }
  .headline { position: absolute; left: 54px; top: 60px; }
  .headline .line-caps { font-family: "Cinzel", serif; font-weight: 700; font-size: 80px; color: var(--navy); line-height: 1; letter-spacing: 1px; }
  .headline .line-to { position: absolute; left: 0; top: 88px; font-family: "Kaushan Script", cursive; font-size: 42px; color: var(--navy); }
  .headline .line-script { position: absolute; left: 92px; top: 56px; font-family: "Dancing Script", cursive; font-weight: 700; font-size: 150px; color: var(--orange); line-height: 1; white-space: nowrap; }
  .about {
    position: absolute; left: 51px; top: 744px; width: 366px;
    color: var(--white); font-size: 17.5px; line-height: 22.6px; text-align: justify;
  }
  .about p + p { margin-top: 22px; }
  .about .name { color: var(--orange); font-weight: 700; }
  .ministries { position: absolute; left: 521px; top: 750px; width: 370px; color: var(--white); }
  .ministries h2 { font-size: 30px; font-weight: 700; color: var(--orange); margin-bottom: 10px; }
  .ministry { position: relative; padding-left: 22px; font-size: 17.5px; line-height: 22.6px; margin-bottom: 10px; }
  .ministry::before {
    content: ""; position: absolute; left: 0; top: 5px;
    border-left: 15px solid var(--orange); border-top: 8px solid transparent; border-bottom: 8px solid transparent;
  }
  .ministry h3 { font-size: 17.5px; font-weight: 700; color: var(--orange); }
  .service {
    position: absolute; left: 514px; top: 1028px; width: 379px; height: 132px;
    background: var(--orange); border-radius: 15px; padding: 9px 0 0 25px;
    color: var(--navy); font-size: 17.5px; line-height: 22.6px;
  }
  .service strong { font-weight: 700; }
  .contact-strip { position: absolute; left: 0; top: 1234px; width: 934px; text-align: center; font-weight: 700; font-size: 23px; line-height: 30px; }
  .contact-strip .invite { color: var(--orange); }
  .contact-strip .details { color: var(--navy); }
</style>
</head>
<body>
<div class="canvas">
  <article class="flyer">
    <div class="hero-photo" role="img" aria-label="Photo of a worship congregation with hands raised toward a lit stage"></div>

    <svg class="backdrop" viewBox="0 0 934 1318" aria-hidden="true">
      <polygon points="0,670 467,694 467,1318 0,1318" fill="#0d3560"/>
      <polygon points="467,694 934,668 934,1318 467,1318" fill="#0b4a78"/>
      <polygon points="0,658 467,684 934,658 934,670 467,697 0,672" fill="#f7941d"/>
      <path d="M0,1230 Q467,1208 934,1230 L934,1318 L0,1318 Z" fill="#e8e9eb"/>
    </svg>

    <div class="brand-tab">
      <span class="brand-dot"></span>
      <span class="brand-name">VOSTI</span>
    </div>

    <header class="headline">
      <div class="line-caps">A VOICE</div>
      <div class="line-to">to the</div>
      <div class="line-script">Nations</div>
    </header>

    <section class="about">
      <p><span class="name">VOSTI</span> is a gathering of believers whose purpose is to seek the face of God for an authentic restoration of the church as a body of born again believers around the world. As a gathering of believers, VOSTI seeks an awakening of the mind founded on the precepts and teachings of Jesus Christ.</p>
      <p>The modern church has replaced the simple and Kingdom centered principles of Jesus's disciples with complacent and compromised teachings on earthly prosperity. We believe in humbly seeking God without motive to use God or His Word for our own gain. The end times church will experience a glorious revival, renewed love and zeal for true discipleship, faith, and godliness as Jesus intended for us.</p>
    </section>

    <section class="ministries">
      <h2>MINISTRIES:</h2>
      <div class="ministry">
        <h3>Kingdom seeds (Children's ministry)</h3>
        <p>Children learn to be seeds of godliness in the world.</p>
      </div>
      <div class="ministry">
        <h3>School of pilgrims</h3>
        <p>Learn the basics of Christian faith and about God's purpose for your life.</p>
      </div>
      <div class="ministry">
        <h3>School of disciples</h3>
        <p>Deepen your knowledge of God's word and learn how to server him.</p>
      </div>
    </section>

    <aside class="service">
      <strong>Sunday Service:</strong><br>
      10:00am-12:30pm<br>
      Linden Community Center<br>
      48 Alder Lane, Portland, ME 04109<br>
      <strong>Visit us at www.vosti.org</strong>
    </aside>

    <footer class="contact-strip">
      <div class="invite">If you need prayer or counseling give us a call at</div>
      <div class="details">+1 207-555-0142 or email us at hello@cedarhollow.org</div>
    </footer>
  </article>
</div>
</body>
</html>
```